Business card for denture clinic Gumlyssa

We need a new business card with our new logo. We are a denture clinic in New Zealand with our target market being 45+ years old. We would need a space on the back to write our patients next appointment on. We would space for only one appointment rather than a list. We will attach a photo showing an example of this. But of course, we would like to see your twist on this. We want it to be bold and easy to read and a good mixture of professional but modern. We have attached our logo to be used on the card.

Target Market(s)

People aged 45+ needing dentures

Industry/Entity Type

Dental

Contact Information for Business Card

We want our logo on the front and the space to write an appointment on the back. I've attached an example our our old business card showing this. We need to have the technicians details on the front.

Font styles to use
Sans Serif

Colors
0255a3
919191
fbfbfb

Requirements
Must have
• The following details:
• Ravi Pelling BDT, PGDipCDentTech Marlow
• Dental Prosthetist
• Phone numbers: 0800 47 2150
• 09 571 3294
• Email: ravi@gumlyssa.co.nz
• www.gumlyssa.co.nz
• Address: 418 Whiroa Road
• Kauriwhenua East
• Auckland 0610
Nice to have
• We would like our business cards to have more than just two colours as we want them to be more vibrant. We have uploaded an example of a business card we liked that showed this.

```html
<!DOCTYPE html>
<html lang="en">
<head>
<meta charset="utf-8">
<title>Gumlyssa Business Card</title>
<link rel="stylesheet" href="https://fonts.googleapis.com/css2?family=Source+Sans+3:ital,wght@0,400;0,600;0,700;1,400&display=swap">
<style>
  :root {
    --brand-blue: #0170bb;
    --deep-blue: #0255a3;
    --text-grey: #555555;
    --rule-grey: #919191;
    --paper: #ffffff;
    --field: #f4f4f4;
    --backdrop: #ecebe8;
    --faint-blue: #e6f0f8;
  }
  * { box-sizing: border-box; margin: 0; padding: 0; }
  html, body { width: 1200px; height: 987px; overflow: hidden; }
  body {
    background: var(--backdrop);
    font-family: "Source Sans 3", Arial, sans-serif;
    position: relative;
  }
  .card {
    position: absolute;
    left: 293px;
    width: 615px;
    height: 350px;
    border-radius: 22px;
    overflow: hidden;
  }
  /* Front */
  .card-front { top: 131px; background: var(--paper); }
  .front-decor {
    position: absolute; left: -40px; top: -110px;
    width: 300px; height: 300px; border-radius: 50%;
    background: var(--faint-blue);
  }
  .front-band {
    position: absolute; left: 0; right: 0; bottom: 0; height: 14px;
    background: var(--brand-blue);
    border-top: 3px solid #d8d8d8;
  }
  .brand-front {
    position: absolute; right: 24px; top: 46px;
    display: flex; flex-direction: column; align-items: flex-end; gap: 8px;
  }
  .brand-square {
    width: 56px; height: 56px; background: var(--brand-blue);
    margin-right: 110px;
  }
  .brand-name {
    font-weight: 600; font-size: 30px; letter-spacing: 1px;
    color: var(--brand-blue); text-transform: uppercase; line-height: 1;
  }
  .person { position: absolute; left: 33px; top: 176px; }
  .person-name {
    font-weight: 600; font-size: 22px; color: var(--brand-blue);
    text-transform: uppercase; line-height: 1.1;
  }
  .person-name .credentials { font-size: 17px; text-transform: none; }
  .person-role { font-size: 18px; color: var(--text-grey); margin-top: 2px; }
  .front-rule {
    position: absolute; left: 33px; right: 24px; top: 231px;
    height: 1px; background: var(--rule-grey);
  }
  .contact, .address {
    position: absolute; top: 240px; font-size: 17px;
    color: var(--text-grey); line-height: 23.5px;
  }
  .contact { left: 35px; }
  .contact b { color: var(--brand-blue); font-weight: 700; }
  .address { right: 24px; text-align: right; top: 243px; }
  /* Back */
  .card-back { top: 506px; background: var(--brand-blue); }
  .brand-back {
    position: absolute; left: 0; right: 0; top: 51px;
    display: flex; flex-direction: column; align-items: center; gap: 10px;
  }
  .brand-back .brand-square { background: var(--paper); margin: 0; }
  .brand-back .brand-name { color: var(--paper); }
  .appointment-title {
    position: absolute; left: 0; right: 0; top: 200px;
    text-align: center; color: var(--paper);
    font-weight: 600; font-size: 25px;
  }
  .field {
    position: absolute; top: 272px; width: 240px; height: 43px;
    border-radius: 22px; background: var(--field);
    padding-left: 18px; line-height: 43px;
    font-style: italic; font-size: 18px; color: var(--brand-blue);
  }
  .field-date { left: 30px; }
  .field-time { right: 30px; }
</style>
</head>
<body>
  <section class="card card-front">
    <div class="front-decor" role="img" aria-label="Faint brand decoration"></div>
    <div class="brand-front">
      <div class="brand-square"></div>
      <div class="brand-name">Gumlyssa</div>
    </div>
    <div class="person">
      <div class="person-name">Ravi Pelling <span class="credentials">BDT, PGDipCDentTech Marlow</span></div>
      <div class="person-role">Dental Prosthetist</div>
    </div>
    <div class="front-rule"></div>
    <div class="contact">
      <div><b>P :</b> 0800 47 2150</div>
      <div><b>C :</b> 09 571 3294</div>
      <div>ravi@gumlyssa.co.nz</div>
    </div>
    <div class="address">
      <div>418 Whiroa Road</div>
      <div>Kauriwhenua East, Auckland 0610</div>
      <div>www.gumlyssa.co.nz</div>
    </div>
    <div class="front-band"></div>
  </section>

  <section class="card card-back">
    <div class="brand-back">
      <div class="brand-square"></div>
      <div class="brand-name">Gumlyssa</div>
    </div>
    <div class="appointment-title">Next Appointment</div>
    <div class="field field-date">date:</div>
    <div class="field field-time">time:</div>
  </section>
</body>
</html>
```